New start-up venture GlenTorvas needs eye-catching, bright, vibrant catering menu design.

GlenTorvas is looking for a tri-fold menu design (6 total pages) for our start-up catering business in Southern New Jersey. Designs should be informative, colorful, appealing, and represent the overall GlenTorvas concept:

“The vision of GLENTORVAS is to provide high quality organic nutrient dense food, juices, and snacks at affordable prices in a positive, fun, and educational environment inspiring a revolution of optimal health and well-being.”

Glentorvas is a Revolutionary catering/take-out concept offering a simple, customizable menu for customers who appreciate a modern approach to traditional food but also place a high priority on health, taste, affordability, and convenience.

Target Market(s)

Glentorvas primary market consists of on-the-go health conscious eaters and those with food allergies. They are deliberate about their eating choices, value quality and convenience, and are willing to pay more for those qualities. We provide Real Food for Real People in the rapidly growing segment of the health conscious dining industry.

Requirements
Must have
• The tri-fold (6 total pages) catering menu brochure must include our name and We Are GlenTorvas logo that has been attached.
You are free to pick and choose our personal pictures of salads, juices, snacks, etc. which are also attached.
The list of various GlenTorvas benefits on the back page of brochure (also added to the uploaded files).
Actual menu items and descriptions (uploaded file section)
Unique, easy to read (legible), fun, and eye-catching font. Please include the following saying, "Real Food for Real People"

Front cover (First page) should be the We Are GlenTorvas logo and space for contact information (You can choose to include pictures of various GlenTorvas, fruits, and vegetables or choose from our personal pictures that are attached)
Pages 2 through 5 should each include our various menu items - all information has been attached:
(Page 2 - Information/pictures with names and descriptions of the GlenTorva smoothies, Page 3 - Information/pictures on the Fresh organic juices with names and descriptions, Page 4 - Information/pictures on the Super Charged Salads with names and descriptions, Page 5 - Information/pictures on additional packaged and prepared menu items)
Page 6 (Back cover - the attached list of various GlenTorva benefits - maybe a picture of the We Are GlenTorvas spinner game - attached file)
Nice to have
• It would be nice for the brochure to incorporate the colors in the GlenTorvas seed of life logo and/or greens, oranges (colors of vegetables). Should you come across a stunning photograph that would benefit brochure, we would entertain that idea of including that photo.
Should not have
• Too much open or empty space.

```html
<!DOCTYPE html>
<html lang="en">
<head>
<meta charset="utf-8">
<title>GlenTorvas Menu</title>
<link rel="stylesheet" href="https://fonts.googleapis.com/css2?family=Lobster&family=Lobster+Two:ital,wght@1,700&family=Raleway:ital,wght@0,400;0,500;1,300;1,400;1,500&display=swap">
<style>
:root{
  --charcoal:#4b4b4d;
  --lime:#8dc63f;
  --lime-pale:#c3dd7a;
  --lime-stripe:#b2d45f;
  --leaf:#6e9b3b;
  --orange:#f7941d;
  --sun:#f3e92a;
  --olive:#a4a03c;
  --olive-text:#f6f0a8;
  --magenta:#e2197c;
  --ink:#1d1d1b;
  --white:#ffffff;
  --soft:#ececec;
}
*{margin:0;padding:0;box-sizing:border-box}
html,body{width:1200px;height:927px;overflow:hidden;background:var(--white)}
.menu{position:relative;width:1200px;height:927px;background:var(--charcoal);font-family:"Raleway",sans-serif;color:var(--soft);overflow:hidden}
.abs{position:absolute}
p{font-style:italic;font-weight:300;font-size:15px;line-height:19px}
.item-name{font-family:"Lobster Two",cursive;font-style:italic;font-weight:700;font-size:20px;color:var(--white)}

/* smoothies panel */
.smoothie-head{left:0;top:0;width:405px;height:96px;background:var(--lime)}
.smoothie-head h2{position:absolute;left:62px;top:14px;font-family:"Lobster Two",cursive;font-style:italic;font-weight:700;font-size:36px;color:var(--ink)}
.smoothie-head .sub{position:absolute;left:28px;top:57px;width:250px;text-align:center;font-size:14.5px;line-height:18px;color:var(--ink);font-weight:500}
.photo-round{border-radius:50%;border:6px solid var(--charcoal)}
.smoothie-photo{left:280px;top:18px;width:128px;height:128px;background:radial-gradient(circle at 45% 45%,#c23a6a,#8c1d4c 55%,#e6dde2 85%)}
.smoothie-list{left:22px;top:104px;width:368px}
.item{margin-bottom:2px}
.smoothie-build{left:0;top:505px;width:405px;height:422px;background:var(--leaf)}
.vertical{writing-mode:vertical-rl;transform:rotate(180deg);font-family:"Lobster Two",cursive;font-style:italic;font-weight:700;white-space:nowrap}
.smoothie-build .vertical{position:absolute;left:10px;top:20px;height:380px;font-size:29px;color:var(--sun);text-align:center}
.build-list{position:absolute;left:62px;top:8px;width:336px;list-style:none;color:var(--lime-pale)}
.build-list li{position:relative;font-style:italic;font-weight:300;font-size:15px;line-height:20px}
.build-list li::before{content:"";position:absolute;left:-12px;top:8px;width:5px;height:5px;border-radius:50%;background:var(--white)}
.build-list b{font-family:"Lobster Two",cursive;font-weight:700;color:var(--white);font-size:17px}

/* centre */
.brand{left:405px;top:0;width:390px;height:185px;background:repeating-linear-gradient(90deg,var(--lime-pale) 0 32px,var(--lime-stripe) 32px 64px)}
.brand-name{position:absolute;left:0;right:0;top:20px;display:flex;justify-content:center;align-items:center;gap:8px;font-size:33px;letter-spacing:1px;color:var(--charcoal);font-weight:400}
.brand-name .dot{width:22px;height:22px;border-radius:50%;background:var(--magenta)}
.brand .menu-word{position:absolute;left:0;right:0;top:46px;text-align:center;font-family:"Lobster",cursive;font-size:110px;line-height:120px;color:var(--magenta)}
.juice-band{left:405px;top:185px;width:390px;height:88px;background:var(--orange);display:flex;align-items:center;justify-content:center}
.juice-band h2{font-family:"Lobster Two",cursive;font-style:italic;font-weight:700;font-size:38px;color:var(--ink)}
.juice-list{left:431px;top:294px;width:345px}
.juice-list .item{margin-bottom:3px}
.extras{left:405px;top:534px;width:390px;text-align:center}
.extras h3{font-family:"Lobster Two",cursive;font-style:italic;font-weight:700;font-size:16px;color:var(--white)}
.extras p{font-size:15px;line-height:15.5px}
.juice-photo{left:411px;top:672px;width:384px;height:255px;background:linear-gradient(90deg,#e0642a 0%,#e49aa4 28%,#6f7a3a 50%,#e9d089 70%,#b3384c 88%),linear-gradient(180deg,#5a3c2a,#b08662);background-blend-mode:multiply}

/* salads */
.salad-head{left:795px;top:0;width:405px;height:96px;background:var(--sun)}
.salad-head h2{position:absolute;right:10px;top:22px;width:240px;text-align:center;font-family:"Lobster Two",cursive;font-style:italic;font-weight:700;font-size:33px;line-height:31px;color:var(--ink)}
.salad-photo{left:797px;top:26px;width:112px;height:120px;border-radius:50%;background:radial-gradient(circle at 50% 50%,#5d7a2e,#3f5a22 40%,#8a5a3a 70%,#d9cdb8)}
.salad-list{left:815px;top:100px;width:370px}
.salad-list p{font-size:15px;line-height:19.2px}
.salad-list .item{margin-bottom:2px}
.salad-list .item-name span{font-family:"Raleway",sans-serif;font-weight:500;font-style:italic;font-size:18px;color:var(--white)}
.salad-build{left:805px;top:652px;width:327px;height:275px;background:var(--olive);color:var(--olive-text)}
.salad-build h3{font-family:"Lobster Two",cursive;font-style:italic;font-weight:700;font-size:17px;color:var(--white);text-align:center}
.cols{display:flex;font-style:italic;font-weight:300;font-size:15px;line-height:15px}
.cols ul{list-style:none}
.dressing{font-size:15px;line-height:17px;font-style:italic;font-weight:300;padding-left:6px}
.dressing b{font-family:"Lobster Two",cursive;font-weight:700;font-size:19px;color:var(--white)}
.salad-vertical{left:1140px;top:652px;width:50px;height:262px;font-size:32px;color:var(--sun);text-align:center}
</style>
</head>
<body>
<main class="menu">

  <header class="abs smoothie-head">
    <h2>Smoothies</h2>
    <div class="sub">BlendPro frozen fruit plant based protein smoothies:</div>
  </header>
  <div class="abs photo-round smoothie-photo" role="img" aria-label="Bowl of red berry smoothie topped with pomegranate seeds"></div>

  <section class="abs smoothie-list">
    <div class="item"><p><span class="item-name">Vanilla Vortex</span> – Frozen fruits include strawberries, pineapple, peaches, mango, and blueberries, Vanilla almond milk, Spirulina Vanilla protein powder, and Vanilla Blueberry Hearth granola clusters</p></div>
    <div class="item"><p><span class="item-name">Strawberry Tsunami</span> - Frozen fruits include strawberries, pineapple, peaches, mango, and blueberries, vanilla coconut milk, Spirulina Strawberry protein powder, and Oat &amp; Honey Hearth granola clusters</p></div>
    <div class="item"><p><span class="item-name">Chocolate Cyclone</span> - Frozen fruits include strawberries, pineapple, peaches, mango, and blueberries, Chocolate almond milk, Spirulina Chocolate protein powder, and Dark Chocolate &amp; Cranberry Hearth granola clusters</p></div>
    <div class="item"><p><span class="item-name">Vanilla Chai Clear Blue Sky</span> – Frozen fruits include strawberries, pineapple, peaches, mango, and blueberries, Vanilla almond/coconut milk blend, Verda Vanilla chai protein powder, and Cinnamon Oat Hearth granola clusters</p></div>
  </section>

  <section class="abs smoothie-build">
    <div class="vertical">Build your own Smoothie</div>
    <ul class="build-list">
      <li>Choice of <b>frozen fruits</b> include strawberries, pineapples, peaches, mango, blue-berries, kiwi, and grapes.</li>
      <li>Choice of <b>plant based, Non-GMO protein powders</b> include Vanilla, Strawberry, and Chocolate Spirulina, Vanilla and Chocolate Sunfield Raw Protein blend, Vanilla Chai Verda One Nutritional Shake, and Meadow Roots Raw Organic Vanilla Protein</li>
      <li>Choice of <b>non-dairy milk alternatives</b> include Vanilla &amp; Chocolate Almond (Sweetened and Unsweetened), Vanilla coconut milk, Vanilla &amp; Chocolate Rice milk, and Vanilla quinoa milk</li>
      <li>Choice of <b>Hearth Granola Clusters</b> include Vanilla Blueberry Clusters, Dark Chocolate &amp; Cranberry Clusters, Maple Walnut Clusters with Chia &amp; Quinoa, and Peanut butter Whole Grain Clusters.</li>
      <li><b>Optional items:</b> Decadent Blend - Chia and Flax Seed with Coconut and Cacoa</li>
    </ul>
  </section>

  <header class="abs brand">
    <div class="brand-name"><span>GLENTORVAS</span><span class="dot"></span></div>
    <div class="menu-word">menu</div>
  </header>
  <div class="abs juice-band"><h2>Fresh Organic Juices</h2></div>

  <section class="abs juice-list">
    <div class="item"><p><span class="item-name">Awakening</span> – Fresh organic blend of Apples, Carrots, and Celery</p></div>
    <div class="item"><p><span class="item-name">Illuminator</span> – Fresh organic blend of Apples, Carrots, Celery, and Kale<br>Enlightenment – Fresh organic blend of Apples, Carrots, and Beets</p></div>
    <div class="item"><p><span class="item-name">Ascension</span> - Fresh organic blend of Apples, Carrots, Celery, Lemon, and Ginger root</p></div>
    <div class="item"><p><span class="item-name">Longevity</span> – Fresh organic blend of Apples, Carrots, Greens, and Brightvale Crimson Goji</p></div>
  </section>

  <section class="abs extras">
    <h3>GlenTorva-Me Optional Items:</h3>
    <p>Aloe Vera water<br>Chia seeds<br>Spirulina<br>Crimson Goji Berry blend</p>
  </section>

  <div class="abs juice-photo" role="img" aria-label="Row of glass mugs filled with orange, pink, green, yellow and red juices on a wooden counter"></div>

  <header class="abs salad-head"><h2>Super<br>Charged Salads</h2></header>
  <div class="abs photo-round salad-photo" role="img" aria-label="Plated green salad surrounded by bowls of seeds and grains"></div>

  <section class="abs salad-list">
    <div class="item"><p style="padding-left:110px"><span class="item-name">Salad #1<span>: Carb Buster</span></span>- Dark</p><p style="padding-left:110px">leafy greens mix AKA:"secret stock",</p><p>asparagus, green beans, broccoli, cauliflower, green apple, spinach, peppers, cucumber, citrus zest, lemon splash and nuts.</p></div>
    <div class="item"><p><span class="item-name">Salad #2<span>: Fruit Delight</span></span>- Dark leafy greens mix, diced mango, berry assortment, sprouts, carrots, organic raisins or cranbits (customer choice).</p></div>
    <div class="item"><p><span class="item-name">Salad #3<span>: Mental Clarity/ Energizer</span></span>- Spinach, Bok Choy, tri-colored bell peppers, beets, blue berries, cabbage duo, orange slices, jicama and sweet potato wedges. Served with savory smooth Turmeric dressing.* Turmeric promotes brain cell stimulation.</p></div>
    <div class="item"><p><span class="item-name">Salad #4<span>: The Diabetic's Friend</span></span>- Dark leafy greens mix, broccoli, cabbage, cauliflower, tomato, avocado, cucumber, onion, spinach, watercress greens, flax, pumpkin and sunflower seeds, beans, nuts and herbs:(cilantro,oregano,basil,mint mixture). This specialty Super Charged Salad comes with a side topping of cinnamon sprinkled apples with museli granola.</p></div>
    <div class="item"><p><span class="item-name">Salad #5<span>: Massaged Kale Protein Booster</span></span>- Kale, edemanme(soy beans), chick peas, finely chopped green beans, dried cherries, sliced almonds, celery leaves, parsley, black beans. This beauty of goodness is served on a layer of spinach leaves.</p></div>
  </section>

  <section class="abs salad-build">
    <h3 style="margin-top:3px">Base Ingredients:</h3>
    <div class="cols" style="padding-left:12px">
      <ul style="width:116px;padding-top:12px"><li>Asparagus</li><li>Arugula</li><li>Avocado</li><li>Beets</li><li>Blueberries</li><li>Broccoli</li></ul>
      <ul style="width:110px;padding-top:12px"><li>Carrots</li><li>Jicama</li><li>Kale</li><li>Mushrooms</li><li>Olives</li><li>Onions</li></ul>
      <ul><li>Radishes</li><li>Romaine</li><li>Spinach</li><li>Sprouts</li><li>Tomatoes</li><li>Watercress</li><li>greens</li></ul>
    </div>
    <h3>Dry Ingredients:</h3>
    <div class="cols" style="padding-left:38px">
      <ul style="width:144px"><li>Chia Seeds</li><li>Cranbits</li><li>Ground Flax</li><li>Goji Berries</li><li>Hemp Seeds</li></ul>
      <ul><li>Pumpkin Seeds</li><li>Sunflower Seeds</li><li>Walnuts</li><li>Pecans</li><li>Almonds</li></ul>
    </div>
    <div class="dressing"><b>Choice of salad dressings:</b> Balsamic Vinaigrette, Valdera onion, Ranch</div>
  </section>
  <div class="abs vertical salad-vertical">Build Your Own</div>

</main>
</body>
</html>
```